Wooden Floor Website

I'd like a Modern and crisp site with emphasis on the site being easy to navigate through - services that we offer, gallery of previous work, history, who we are, contact, etc
https://vaultqx8261937-my.filedeckly.com/:b:/g/personal/tobias_pellwickhaus_co_uk/QWM7R2_kpLsTbNVafrxHoZWCKdYeP8u3G6vRPMsLmoXBtc

Coded - Design and coding required

5+ page

• Word Press Site

```html
<!DOCTYPE html>
<html lang="en">
<head>
<meta charset="utf-8">
<title>Pellwickhaus – Wooden Floors</title>
<link rel="stylesheet" href="https://fonts.googleapis.com/css2?family=IBM+Plex+Sans:wght@400;500;600;700&display=swap">
<style>
:root{
  --ink:#2b2b2b;
  --text:#4a4a4a;
  --white:#ffffff;
  --light:#cfcfcf;
  --field:#d2d2d2;
  --dark:#3c3c3c;
  --hero-a:#3a3836;
  --hero-b:#1f1e1d;
  --line:rgba(255,255,255,.35);
}
*{box-sizing:border-box;margin:0;padding:0}
html,body{width:1200px;height:3107px;overflow:hidden}
body{font-family:"IBM Plex Sans",Arial,sans-serif;color:var(--ink);background:var(--white);position:relative}
.abs{position:absolute}

/* hero */
.hero{left:0;top:0;width:1200px;height:740px;background:linear-gradient(160deg,var(--hero-a) 0%,#2d2b29 45%,var(--hero-b) 100%)}
.hero-photo{inset:0;background:radial-gradient(ellipse at 75% 30%,rgba(120,120,118,.45),transparent 55%),linear-gradient(180deg,rgba(70,58,46,.35) 0%,rgba(30,28,26,.2) 50%,rgba(20,18,16,.55) 100%)}
.brand{left:30px;top:24px;display:flex;align-items:center;gap:10px;color:var(--white);font-weight:600;font-size:13px;letter-spacing:.5px}
.brand-dot{width:14px;height:14px;border-radius:50%;background:var(--white)}
.nav{right:0;top:24px;width:680px;display:flex;gap:34px;padding-left:80px}
.nav a{color:var(--white);font-size:15px;font-weight:600;text-decoration:none}
.guide{top:0;width:1px;height:740px;background:var(--line)}
.hero-title{left:182px;top:330px;color:#e8e8e8;font-size:70px;font-weight:700;line-height:1}
.hero-sub{left:196px;top:412px;color:#e2e2e2;font-size:36px;font-weight:400}
.hero-tag{left:604px;top:566px;color:#e6e6e6;font-size:22px}
.hero-rule{left:592px;height:1px;background:var(--line)}
.social{left:1131px;width:24px;height:24px;border:2px solid var(--white);border-radius:50%}

/* who we are */
.who{left:0;top:740px;width:1200px;height:515px;background:var(--light)}
.heading{font-size:38px;font-weight:700;color:var(--ink);letter-spacing:.5px}
.copy{font-size:13px;line-height:16px;color:var(--text)}
.who-rule{left:177px;top:405px;width:536px;height:1px;background:#555}

/* gallery */
.gallery{left:0;top:1255px;width:1200px;height:687px;background:var(--white)}
.gallery-label{left:42px;top:240px;font-size:21px;font-weight:700;line-height:27px;color:#111}
.panel{top:0;width:256px;height:687px}
.panel-num{position:absolute;left:22px;top:215px;font-size:56px;font-weight:700;color:var(--white);line-height:1}
.panel-name{position:absolute;left:26px;top:290px;font-size:16px;line-height:22px;color:var(--white)}
.pager-btn{top:637px;width:24px;height:24px;border-radius:50%;background:var(--white)}
.pager-count{left:322px;top:610px;color:var(--white);font-size:20px;font-weight:600}
.pager-track{left:322px;top:648px;width:423px;height:1px;background:rgba(255,255,255,.4)}
.pager-fill{left:345px;top:647px;width:30px;height:3px;background:var(--white)}

/* history */
.history{left:0;top:1942px;width:1200px;height:544px;background:var(--light)}
.btn-more{left:177px;top:394px;width:86px;height:20px;border:1.5px solid #555;border-radius:3px;font-size:11px;line-height:17px;text-align:center;color:#333}
.person{left:740px;top:66px;width:337px;height:375px;background:linear-gradient(180deg,#c9a27e 0%,#6f9fd1 45%,#3f79bb 100%);border-radius:4px}

/* contact */
.contact{left:0;top:2486px;width:1200px;height:621px;background:linear-gradient(180deg,#4a4a4a,var(--dark))}
.contact-title{left:0;width:1097px;top:68px;text-align:center;color:var(--white);font-size:38px;font-weight:700}
.form{left:219px;top:170px;width:431px;height:336px;background:var(--white);border-radius:8px}
.field-label{position:absolute;left:30px;font-size:13px;color:#444}
.field{position:absolute;left:30px;width:371px;height:32px;background:var(--field);border-radius:4px}
.info{left:688px;top:170px;width:247px;height:336px;border:2px solid var(--white);border-radius:8px;color:var(--white);padding:26px 20px}
.info dt{font-size:14px;margin-top:22px}
.info dt:first-child{margin-top:0}
.info dd{font-size:14px;font-weight:700;margin-top:8px;line-height:17px}
</style>
</head>
<body>

<header class="abs hero">
  <div class="abs hero-photo" role="img" aria-label="Dark kitchen and dining room with wooden floor and black chairs"></div>
  <div class="abs brand"><span class="brand-dot"></span>PELLWICKHAUS</div>
  <nav class="abs nav"><a href="#">Home</a><a href="#">About</a><a href="#">Blog</a><a href="#">Services</a><a href="#">Contact Us</a></nav>
  <div class="abs guide" style="left:175px"></div>
  <div class="abs guide" style="left:1008px"></div>
  <h1 class="abs hero-title">THE BEST</h1>
  <p class="abs hero-sub">flooring ideas and products</p>
  <div class="abs hero-rule" style="top:540px;width:416px"></div>
  <p class="abs hero-tag">We Believe In Excellence</p>
  <div class="abs hero-rule" style="top:620px;width:416px"></div>
  <span class="abs social" style="top:321px"></span>
  <span class="abs social" style="top:365px"></span>
  <span class="abs social" style="top:404px"></span>
</header>

<section class="abs who">
  <h2 class="abs heading" style="left:177px;top:92px">WHO WE ARE</h2>
  <p class="abs copy" style="left:177px;top:156px;width:830px">Lorem ipsum dolor sit amet, consectetur adipiscing elit. Nam vehicula est ut suscipit lacinia. Duis erat lectus, luctus sed cursus a, vene natis sit amet diam. Phasellus iaculis interdum urna id dignissim. Vestibulum vel nibh at felis lacinia dignissim at vel neque. Orci varius natoque penatibus et magnis dis parturient montes, nascetur ridiculus mus. Quisque non gravida nulla, quis auctor turpis. A erean non sem nulla. Ut non sollicitudin lacus, a efficitur turpis. Mauris varius fringilla neque quis fermentum. Duis eget rutrum justo. Morbi dignissim posuere odio, nec viverra sapien dapibus id. Sed vitae lacus sed risus molestie convallis. Duis vitae pell entesque libero.</p>
  <p class="abs copy" style="left:177px;top:276px;width:830px">Lorem ipsum dolor sit amet, consectetur adipiscing elit. Nam vehicula est ut suscipit lacinia. Duis erat lectus, luctus sed cursus a, vene natis sit amet diam. Phasellus iaculis interdum urna id dignissim. Vestibulum vel nibh at felis lacinia dignissim at vel neque. Orci varius natoque penatibus et magnis dis parturient montes, nascetur ridiculus mus. Quisque non gravida nulla, quis auctor turpis. A erean non sem nulla. Ut non sollicitudin lacus, a efficitur turpis. Mauris varius fringilla neque quis fermentum. Duis eget rutrum justo. Morbi dignissim posuere odio, nec viverra sapien dapibus id. Sed vitae lacus sed risus molestie convallis. Duis vitae pell entesque libero.</p>
  <div class="abs who-rule"></div>
</section>

<section class="abs gallery">
  <h2 class="abs gallery-label">Gallery<br>of<br>previous<br>work</h2>
  <div class="abs panel" style="left:175px;background:linear-gradient(180deg,#c9c6c1 0%,#a08366 55%,#7a5a3e 100%)" role="img" aria-label="Bedroom with light oak floor">
    <span class="panel-num">06</span><span class="panel-name">Ashford<br>Meadow<br>Oak</span></div>
  <div class="abs panel" style="left:431px;background:linear-gradient(180deg,#5d6848 0%,#4a4038 50%,#3a3330 100%)" role="img" aria-label="Mid-tone oak floor with plant and side table">
    <span class="panel-num">07</span><span class="panel-name">Tenby<br>Mono<br>Oak</span></div>
  <div class="abs panel" style="left:687px;background:linear-gradient(180deg,#2d3a55 0%,#5a5a5c 40%,#3c3b3b 100%)" role="img" aria-label="Dining room with dark ash floor">
    <span class="panel-num">08</span><span class="panel-name">Radley<br>Ash<br>Oak</span></div>
  <div class="abs panel" style="left:943px;width:257px;background:linear-gradient(180deg,#c4c4c6 0%,#6f6d6c 55%,#474544 100%)" role="img" aria-label="Hallway with grey oak floor">
    <span class="panel-num">09</span><span class="panel-name">Corwen<br>Storm<br>Oak</span></div>
  <span class="abs pager-btn" style="left:203px"></span>
  <span class="abs pager-btn" style="left:235px"></span>
  <span class="abs pager-count">06 / 96</span>
  <div class="abs pager-track"></div>
  <div class="abs pager-fill"></div>
</section>

<section class="abs history">
  <h2 class="abs heading" style="left:177px;top:130px">OUR HISTORY</h2>
  <p class="abs copy" style="left:177px;top:213px;width:420px">Lorem ipsum dolor sit amet, consectetur adipiscing elit. Nam vehicula est ut suscipit lacinia. Duis erat lectus, luctus sed cursus a, vene natis sit amet diam. Phasellus iaculis interdum urna id dignissim. Vestibulum vel nibh at felis lacinia dignissim at vel neque. Orci varius natoque penatibus et magnis dis parturient montes, nascetur ridiculus mus. Quisque non gravida nulla, quis auctor turpis. A erean non sem nulla. Ut non sollicitudin lacus, a efficitur turpis. Mauris varius fringilla neque quis fermentum. Duis eget rutrum justo. Morbi dignissim posuere odio, nec viverra sapien dapibus id. Sed vitae lacus sed risus molestie convallis. Duis vitae pell entesque libero.</p>
  <span class="abs btn-more">Read More</span>
  <div class="abs person" role="img" aria-label="Smiling man in a denim shirt pointing to the left"></div>
</section>

<section class="abs contact">
  <h2 class="abs contact-title">CONTACT US</h2>
  <form class="abs form">
    <span class="field-label" style="top:24px">NAME</span>
    <span class="field" style="top:50px"></span>
    <span class="field-label" style="top:94px">EMAIL</span>
    <span class="field" style="top:118px"></span>
    <span class="field-label" style="top:162px">MESSAGE</span>
    <span class="field" style="top:188px;height:120px"></span>
  </form>
  <dl class="abs info">
    <dt>email</dt><dd>info@pellwickhaus.com</dd>
    <dt>Phone no#</dt><dd>0770135548219</dd>
    <dt>Address</dt><dd>KRB<br>12th Row<br>4810<br>Eastvale</dd>
  </dl>
</section>

</body>
</html>
```